Tavrento - Staffing APP for the hospitality industry.

I need 7 screens designed that form the core of the APP. Tavrento is a staffing APP for the hospitality industry where workers sign up and complete details about themselves and their qualifications and experience. They also switch a button ON and OFF showing their availability status. Venues/employers then scan for workers based on job type, availability, distance etc

Industry/Entity Type

Hospitality employment industry

Number of Pages Required

5+ page

Requirements
Must have
• Refer wire frames supplied
Nice to have
• Here is my website as a guide www.tavrento.com.au
Should not have
• Nil

```html
<!DOCTYPE html>
<html lang="en">
<head>
<meta charset="utf-8">
<title>Tavrento – App Screens</title>
<link href="https://fonts.googleapis.com/css2?family=Poppins:wght@400;500;600;700&display=swap" rel="stylesheet">
<style>
:root{
  --canvas:#333437;
  --glow:rgba(120,100,40,.35);
  --screen:#2b2c2f;
  --status:#27282b;
  --field:#38393c;
  --field-line:#47484c;
  --text:#ffffff;
  --muted:#8d8e92;
  --accent:#fdc300;
  --dark-text:#1e1e20;
}
*{box-sizing:border-box;margin:0;padding:0}
html,body{width:1200px;height:3000px;overflow:hidden;background:var(--canvas)}
body{font-family:'Poppins',sans-serif;color:var(--text)}
.stage{position:absolute;left:0;top:0;width:1030px;height:2576px;transform:scale(1.16505);transform-origin:0 0;
  background:radial-gradient(ellipse 55% 45% at 50% 50%,var(--glow),transparent 80%),var(--canvas)}
.screen{position:absolute;width:258px;height:557px;background:var(--screen);border-radius:14px;overflow:hidden;
  box-shadow:0 10px 40px rgba(0,0,0,.35)}
.status{position:absolute;left:0;top:0;width:100%;height:24px;background:var(--status);font-size:9px;font-weight:500}
.status .time{position:absolute;left:10px;top:7px}
.status .sys{position:absolute;right:10px;top:6px;display:flex;align-items:center;gap:3px}
.abs{position:absolute}
.title{position:absolute;left:9px;font-size:16px;font-weight:600}
.title em{font-style:normal;color:var(--accent)}
.field{position:absolute;background:var(--field);border:1px solid var(--field-line);border-radius:3px;
  font-size:8px;color:var(--muted);padding:0 8px;display:flex;align-items:center}
.field.tall{align-items:flex-start;padding-top:8px}
.field .caret{position:absolute;right:9px;top:50%;margin-top:-2px;width:0;height:0;border-left:2px solid transparent;border-right:2px solid transparent;border-top:3px solid var(--accent)}
.field .count{position:absolute;right:12px;bottom:12px;font-size:8px}
.label{position:absolute;font-size:8px;color:var(--text)}
.label.sub{font-size:9px;color:#c8c8cb}
.btn{position:absolute;height:29px;background:var(--accent);color:var(--dark-text);border-radius:3px;font-size:9px;font-weight:600;
  display:flex;align-items:center;justify-content:center}
.btn.ghost{background:transparent;border:1px solid var(--accent);color:var(--accent)}
.btn.ghost.light{color:var(--text)}
.radio{position:absolute;font-size:5px;display:flex;gap:7px;color:#c8c8cb}
.radio span::before{content:"";display:inline-block;width:3px;height:3px;border:1px solid var(--accent);border-radius:50%;margin-right:2px;vertical-align:middle}
.radio span.on::before{background:var(--accent)}
.photo{position:absolute;border-radius:3px;background:linear-gradient(180deg,#35363a 0%,#2e2f33 55%,#1f2440 100%);box-shadow:0 2px 8px rgba(0,0,0,.4)}
.card{position:absolute;left:9px;top:82px;width:239px;height:318px;background:#303134;border:1px solid #3d3e42;border-radius:3px;box-shadow:0 4px 14px rgba(0,0,0,.35)}
.scan-note{position:absolute;width:100%;top:11px;text-align:center;font-size:7px;font-weight:600}
.scan-note em{font-style:normal;color:var(--accent)}
.meta{position:absolute;top:186px;width:100%;font-size:8px;font-weight:600}
.stats{position:absolute;font-size:9px;font-weight:600}
.stats .y{color:var(--accent)}
.stats .n{color:var(--muted)}
.icon{position:absolute;width:18px;height:18px;border-radius:50%;background:#414246;display:flex;align-items:center;justify-content:center}
</style>
</head>
<body>
<div class="stage">

<!-- Splash -->
<section class="screen" style="left:222px;top:86px">
  <div class="status" style="background:var(--screen)"><span class="time">9:10</span><span class="sys">▾ ıll 69% ▮</span></div>
  <div class="abs" style="left:56px;top:169px;width:146px;height:146px;border-radius:50%;background:#333438;box-shadow:0 6px 18px rgba(0,0,0,.45),inset 0 0 0 1px #3e3f43;display:flex;align-items:center;justify-content:center">
    <span style="color:var(--accent);font-size:27px;font-weight:600">Tavrento</span>
  </div>
  <p class="abs" style="left:0;width:100%;top:339px;text-align:center;font-size:10px">Staffing APP for the hospitality industry.</p>
  <p class="abs" style="left:0;width:100%;top:496px;text-align:center;font-size:14px;font-weight:600;color:var(--accent)">Get Started →</p>
</section>

<!-- Worker registration -->
<section class="screen" style="left:550px;top:86px">
  <div class="status"><span class="time">9:10</span><span class="sys">▾ ıll 69% ▮</span></div>
  <h1 class="title" style="top:43px"><em>Workers</em> Registreation</h1>
  <div class="field" style="left:9px;top:73px;width:239px;height:28px">First Name</div>
  <div class="field" style="left:9px;top:107px;width:239px;height:28px">Mobile Number</div>
  <div class="field" style="left:9px;top:141px;width:239px;height:28px">Email Address</div>
  <span class="label sub" style="left:9px;top:181px">Location</span>
  <div class="field" style="left:9px;top:198px;width:117px;height:28px">Street Number</div>
  <div class="field" style="left:130px;top:198px;width:118px;height:28px">Street name</div>
  <div class="field" style="left:9px;top:232px;width:117px;height:28px">City</div>
  <div class="field" style="left:130px;top:232px;width:118px;height:28px">State</div>
  <div class="field" style="left:9px;top:266px;width:239px;height:28px">Postal code</div>
  <div class="field" style="left:9px;top:300px;width:239px;height:65px"></div>
  <div class="abs" role="img" aria-label="Profile image placeholder" style="left:16px;top:306px;width:52px;height:52px;border-radius:50%;background:linear-gradient(180deg,#e9ecef 45%,#4caf50 46%)"></div>
  <div class="btn" style="left:130px;top:322px;width:79px;height:21px;font-size:8px;font-weight:500">Upload Image</div>
  <span class="label" style="left:9px;top:380px">Date of birth</span>
  <div class="field" style="left:130px;top:372px;width:118px;height:28px">DD/MM/YYYY</div>
  <span class="label" style="left:9px;top:415px">RSA</span>
  <div class="radio" style="left:41px;top:417px"><span class="on">Yes</span><span>No</span></div>
  <span class="label" style="left:130px;top:415px">SFA</span>
  <div class="radio" style="left:161px;top:417px"><span>Yes</span><span class="on">No</span></div>
  <span class="label" style="left:9px;top:447px">Vaccination Status</span>
  <div class="field" style="left:130px;top:438px;width:118px;height:28px">Vaccinated<i class="caret"></i></div>
  <span class="label" style="left:9px;top:474px;line-height:12px">Eligible to work<br>in austrilia</span>
  <div class="radio" style="left:75px;top:483px"><span class="on">Yes</span><span>No</span></div>
  <span class="label" style="left:130px;top:481px">ABN</span>
  <div class="radio" style="left:161px;top:483px"><span>Yes</span><span class="on">No</span></div>
  <div class="btn" style="left:9px;top:506px;width:239px">NEXT</div>
</section>

<!-- Qualifications -->
<section class="screen" style="left:222px;top:703px">
  <div class="status"><span class="time">9:10</span><span class="sys">▾ ıll 69% ▮</span></div>
  <span class="label" style="left:9px;top:45px">Qualification</span>
  <div class="field" style="left:9px;top:63px;width:239px;height:164px"><span class="count">500 words</span></div>
  <span class="label" style="left:9px;top:243px">Experience</span>
  <div class="field" style="left:9px;top:261px;width:239px;height:164px"><span class="count">500 words</span></div>
  <span class="label" style="left:9px;top:460px">Select Category</span>
  <div class="field" style="left:130px;top:451px;width:118px;height:28px">Your Category<i class="caret"></i></div>
  <div class="btn" style="left:9px;top:505px;width:239px">Register</div>
</section>

<!-- Employer home -->
<section class="screen" style="left:550px;top:703px">
  <div class="status"><span class="time">9:10</span><span class="sys">▾ ıll 69% ▮</span></div>
  <h1 class="title" style="top:42px"><em>Employer</em> Home</h1>
  <div class="btn" style="left:221px;top:43px;width:27px;height:20px;font-size:7px">Edit</div>
  <div class="field" style="left:9px;top:84px;width:239px;height:28px">Venue Name</div>
  <div class="field" style="left:9px;top:120px;width:239px;height:28px">Contact &nbsp;Person</div>
  <div class="field" style="left:9px;top:156px;width:239px;height:28px">Email address</div>
  <div class="field" style="left:9px;top:192px;width:239px;height:28px">Mobile Number</div>
  <div class="field tall" style="left:9px;top:228px;width:239px;height:123px">Location</div>
  <div class="btn ghost light" style="left:9px;top:359px;width:239px;height:28px;font-size:11px;font-weight:400">Lecal + Payment</div>
  <div class="btn ghost" style="left:9px;top:505px;width:117px">Scan Favourites</div>
  <div class="btn" style="left:131px;top:505px;width:117px">Scan Workers</div>
</section>

<!-- Scan workers -->
<section class="screen" style="left:222px;top:1318px">
  <div class="status"><span class="time">9:10</span><span class="sys">▾ ıll 69% ▮</span></div>
  <h1 class="title" style="top:43px">Scan <em>Workers</em></h1>
  <p class="abs" style="left:9px;top:97px;font-size:15px">Select filters</p>
  <span class="label" style="left:9px;top:134px">Job Type</span>
  <div class="field" style="left:130px;top:125px;width:118px;height:28px">JOb<i class="caret"></i></div>
  <span class="label" style="left:9px;top:170px">Available Now</span>
  <div class="field" style="left:130px;top:161px;width:118px;height:28px"><div class="radio" style="left:30px;top:11px;gap:24px"><span class="on">Yes</span><span>No</span></div></div>
  <span class="label" style="left:9px;top:206px">Distance</span>
  <div class="field" style="left:130px;top:197px;width:118px;height:28px">15 km</div>
  <span class="label" style="left:9px;top:242px">Sort By</span>
  <div class="field" style="left:130px;top:233px;width:118px;height:28px">sor by name<i class="caret"></i></div>
  <div class="btn" style="left:9px;top:506px;width:239px">Start Scan</div>
</section>

<!-- Scan result -->
<section class="screen" style="left:550px;top:1318px">
  <div class="status"><span class="time">9:10</span><span class="sys">▾ ıll 69% ▮</span></div>
  <h1 class="title" style="top:42px">Scan <em>Result</em></h1>
  <div class="card">
    <p class="scan-note">Last scan <em>2 hrs ago</em></p>
    <div class="photo" role="img" aria-label="Worker profile photo" style="left:33px;top:32px;width:173px;height:140px"></div>
    <div class="meta"><span class="abs" style="left:52px">Peter &nbsp;28</span><span class="abs" style="left:121px">|</span><span class="abs" style="left:155px">16 kms</span></div>
    <div class="stats" style="left:31px;top:218px">RSA</div><div class="stats y" style="left:91px;top:218px">Yes</div>
    <div class="stats" style="left:128px;top:218px">SFH</div><div class="stats y" style="left:187px;top:218px">Yes</div>
    <div class="stats" style="left:31px;top:236px">Vax status</div><div class="stats y" style="left:91px;top:236px">Full</div>
    <div class="stats" style="left:128px;top:236px">ABN</div><div class="stats n" style="left:187px;top:236px">No</div>
    <div class="btn ghost light" style="left:7px;top:278px;width:111px;font-size:8px;font-weight:400">View Qualification</div>
    <div class="btn ghost light" style="left:121px;top:278px;width:111px;font-size:8px;font-weight:400">View Experience</div>
  </div>
  <div class="icon" style="left:38px;top:482px"><svg width="10" height="10" viewBox="0 0 10 10"><path d="M5 .5l1.4 2.9 3.1.4-2.3 2.2.6 3.1L5 7.6 2.2 9.1l.6-3.1L.5 3.8l3.1-.4z" fill="var(--accent)"/></svg></div>
  <div class="icon" style="left:119px;top:482px"><svg width="10" height="8" viewBox="0 0 10 8"><path d="M.5 4C2 1.5 3.5.8 5 .8S8 1.5 9.5 4C8 6.5 6.5 7.2 5 7.2S2 6.5.5 4z" fill="none" stroke="var(--accent)"/><circle cx="5" cy="4" r="1.4" fill="var(--accent)"/></svg></div>
  <div class="icon" style="left:201px;top:482px"><svg width="10" height="10" viewBox="0 0 10 10"><path d="M1 5h8M5.5 1.5 9 5 5.5 8.5" fill="none" stroke="var(--accent)" stroke-width="1.2"/></svg></div>
  <div class="btn" style="left:9px;top:506px;width:76px;font-size:7px">Add to favourites</div>
  <div class="btn" style="left:90px;top:506px;width:77px;font-size:7px">Reveal</div>
  <div class="btn" style="left:172px;top:506px;width:76px;font-size:7px">Next</div>
</section>

<!-- Favourites -->
<section class="screen" style="left:373px;top:1933px">
  <div class="status"><span class="time">9:10</span><span class="sys">▾ ıll 69% ▮</span></div>
  <h1 class="title" style="top:44px"><em>Favourites</em></h1>
  <div class="card" style="top:83px">
    <p class="scan-note">Last scan <em>2 days ago</em></p>
    <div class="photo" role="img" aria-label="Worker profile photo" style="left:33px;top:32px;width:173px;height:140px"></div>
    <div class="meta"><span class="abs" style="left:52px">Peter &nbsp;28</span><span class="abs" style="left:121px">|</span><span class="abs" style="left:155px">16 kms</span></div>
    <div class="stats" style="left:31px;top:218px">RSA</div><div class="stats y" style="left:91px;top:218px">Yes</div>
    <div class="stats" style="left:128px;top:218px">SFH</div><div class="stats y" style="left:187px;top:218px">Yes</div>
    <div class="stats" style="left:31px;top:236px">Vax status</div><div class="stats y" style="left:91px;top:236px">Full</div>
    <div class="stats" style="left:128px;top:236px">ABN</div><div class="stats n" style="left:187px;top:236px">No</div>
    <div class="btn ghost light" style="left:7px;top:278px;width:111px;font-size:8px;font-weight:400">View Qualification</div>
    <div class="btn ghost light" style="left:121px;top:278px;width:111px;font-size:8px;font-weight:400">View Experience</div>
  </div>
  <div class="icon" style="left:59px;top:483px"><svg width="10" height="8" viewBox="0 0 10 8"><path d="M.5 4C2 1.5 3.5.8 5 .8S8 1.5 9.5 4C8 6.5 6.5 7.2 5 7.2S2 6.5.5 4z" fill="none" stroke="var(--accent)"/><circle cx="5" cy="4" r="1.4" fill="var(--accent)"/></svg></div>
  <div class="icon" style="left:181px;top:483px"><svg width="10" height="10" viewBox="0 0 10 10"><path d="M1 5h8M5.5 1.5 9 5 5.5 8.5" fill="none" stroke="var(--accent)" stroke-width="1.2"/></svg></div>
  <div class="btn" style="left:9px;top:507px;width:118px;font-size:7px">Reveal</div>
  <div class="btn" style="left:132px;top:507px;width:116px;font-size:7px">Next</div>
</section>

</div>
</body>
</html>
```